I need a flyer made , the flyer can be one page or two pages or three pages . I will be posting this on Instagram and social media platforms. I am a luxury home builder , I am looking to hire a construction project manager . Below are some examples and ideas what can be on the flyer

We’re looking for a construction project manager who’s passionate about building luxury homes at the highest standards
We’re hiring construction project manager
* Experience 5+ years in residential project management with a strong portfolio of completed homes.
* location : Bergen County NJ
* excellent leadership skills, leads teams with confidence and clarity
* communicates seamlessly with architects , engineers, designers and clients
*knows how to manage budgets and timelines without compromising quality
*solves problems with a positive solution first mindset
* pays attention to every detail because in luxury the small things are the big things

Apply now , link in bio or DM to connect.

My logo is attached, my web site www.ridgelanebuilders.com
My style is modern but still warm and inviting. I like a clean classy look .
Updates

Please don’t add any images of chairs or people to the flyer , I do not want people on my flyer. Do not add standard images of offices and houses , we are luxury builders , we build homes over 2 million dollars. Keep a classy , simple modern look . High end .

You can add a white hard hat with my logo on it for a image , this is a suggestion does not have to be on my flyer ,

```html
<!DOCTYPE html>
<html lang="en">
<head>
<meta charset="UTF-8">
<title>Ridgelane Builders – Construction Project Manager</title>
<link href="https://fonts.googleapis.com/css2?family=Jost:wght@400;500;600;700;800&family=Open+Sans:wght@400;700&display=swap" rel="stylesheet">
<style>
  :root {
    --ink: #111111;
    --paper: #ffffff;
    --band: #e1e4e6;
    --sky: #6f9fd6;
    --timber: #c79a66;
    --gravel: #55585c;
  }
  * { margin: 0; padding: 0; box-sizing: border-box; }
  html, body {
    width: 960px; height: 1200px; overflow: hidden;
    background: var(--paper);
  }
  .flyer {
    position: relative; width: 960px; height: 1200px;
    background: var(--paper); color: var(--ink);
    font-family: "Jost", sans-serif;
  }
  .brand {
    position: absolute; left: 265px; top: 48px;
    width: 430px; height: 184px;
    background: var(--ink);
    display: flex; align-items: center; justify-content: center;
  }
  .brand-name {
    color: var(--paper); font-family: "Jost", sans-serif;
    font-weight: 400; font-size: 40px; letter-spacing: 4px;
    text-transform: uppercase;
  }
  .intro {
    position: absolute; left: 0; top: 266px; width: 960px;
    text-align: center; font-size: 27px; font-weight: 400;
    line-height: 43px; text-transform: uppercase; letter-spacing: -0.2px;
  }
  .hero-band {
    position: absolute; left: 0; top: 414px; width: 960px; height: 263px;
    background: var(--band);
  }
  .site-photo {
    position: absolute; left: 76px; top: 9px; width: 391px; height: 245px;
    background: linear-gradient(180deg, var(--sky) 0%, #a9c4e2 22%, var(--timber) 40%, #b78a58 78%, var(--gravel) 100%);
  }
  .hero-title {
    position: absolute; left: 500px; top: 4px;
    text-transform: uppercase; line-height: 1;
  }
  .hero-we { font-size: 94px; font-weight: 400; letter-spacing: 2px; display: block; }
  .hero-hiring { font-size: 98px; font-weight: 800; letter-spacing: 2px; display: block; margin-top: -6px; }
  .hero-construction { font-size: 38px; font-weight: 700; letter-spacing: 6.4px; display: block; margin-top: 6px; }
  .hero-role { font-size: 39px; font-weight: 400; letter-spacing: 1.4px; display: block; margin-top: 6px; }
  .requirements {
    position: absolute; left: 82px; top: 731px; width: 830px;
    list-style: none; text-transform: uppercase;
    font-size: 16.5px; line-height: 34.5px; font-weight: 400;
  }
  .requirements li { position: relative; padding-left: 24px; }
  .requirements li::before {
    content: ""; position: absolute; left: 0; top: 14px;
    width: 10px; height: 10px; border-radius: 50%; background: var(--ink);
  }
  .requirements .wrap { display: block; margin-left: -24px; }
  .cta {
    position: absolute; left: 0; top: 1080px; width: 960px; text-align: center;
  }
  .cta-line { font-family: "Open Sans", sans-serif; font-weight: 700; font-size: 26px; }
  .cta-url { font-size: 19px; text-transform: uppercase; margin-top: 4px; }
  .cta-rule {
    position: absolute; left: 316px; top: 1143px; width: 330px; height: 12px;
    background: var(--ink);
  }
</style>
</head>
<body>
<main class="flyer">
  <div class="brand"><span class="brand-name">Ridgelane Builders</span></div>

  <p class="intro">We’re looking for a construction project manager<br>who’s passionate about building luxury homes<br>at the highest standards</p>

  <section class="hero-band">
    <div class="site-photo" role="img" aria-label="Timber-framed luxury home under construction against a blue sky, with a gravel pile in front"></div>
    <h1 class="hero-title">
      <span class="hero-we">We’re</span>
      <span class="hero-hiring">Hiring</span>
      <span class="hero-construction">Construction</span>
      <span class="hero-role">Project Manager</span>
    </h1>
  </section>

  <ul class="requirements">
    <li>Experience 5+ years in residential project management with a strong<span class="wrap">portfolio of completed homes.</span></li>
    <li>Location : Bergen County NJ</li>
    <li>Excellent leadership skills, leads teams with confidence and clarity</li>
    <li>Communicates seamlessly with architects , engineers, designers and clients</li>
    <li>Knows how to manage budgets and timelines without compromising quality</li>
    <li>Solves problems with a positive solution first mindset</li>
    <li>Pays attention to every detail because in luxury the small things are<span class="wrap">the big things</span></li>
  </ul>

  <div class="cta">
    <p class="cta-line">Apply now , link in bio or DM to connect.</p>
    <p class="cta-url">www.ridgelanebuilders.com</p>
  </div>
  <div class="cta-rule"></div>
</main>
</body>
</html>
```